Diagram of Marrowfen’s history for website

This project is to design the attached diagram along the lines of the attached image but in our branding - style guide attached. The diagram will be going on the Marrowfen website - www.marrowfen.au.

```html
<!DOCTYPE html>
<html lang="en">
<head>
<meta charset="utf-8">
<title>Our History – Marrowfen</title>
<link rel="stylesheet" href="https://fonts.googleapis.com/css2?family=Poppins:wght@300;400;500;600&display=swap">
<style>
  :root {
    --sage: #748c73;
    --slate: #7e9ea6;
    --clay: #d2ae9c;
    --ink: #3a3a3a;
    --body: #3f3f3f;
    --paper: #ffffff;
  }
  * { margin: 0; padding: 0; box-sizing: border-box; }
  html, body { width: 1200px; height: 806px; overflow: hidden; background: var(--paper); }
  .history {
    position: relative;
    width: 1200px;
    height: 806px;
    font-family: "Poppins", sans-serif;
    color: var(--body);
  }
  .timeline-art { position: absolute; left: 0; top: 0; }
  .title {
    position: absolute;
    left: 98px;
    top: 66px;
    font-size: 52px;
    font-weight: 600;
    line-height: 37px;
    color: var(--ink);
    letter-spacing: -0.5px;
  }
  .title span { display: block; }
  .entry { position: absolute; width: 170px; }
  .year {
    position: absolute;
    font-size: 25px;
    font-weight: 400;
    line-height: 28px;
    letter-spacing: 0.3px;
  }
  .heading {
    position: absolute;
    font-size: 18.5px;
    font-weight: 500;
    line-height: 16px;
    letter-spacing: 0.2px;
    white-space: nowrap;
  }
  .summary {
    position: absolute;
    font-size: 11.3px;
    font-weight: 300;
    line-height: 15px;
    white-space: nowrap;
    color: var(--body);
  }
  .is-sage { color: var(--sage); }
  .is-slate { color: var(--slate); }
</style>
</head>
<body>
<main class="history">
  <svg class="timeline-art" width="1200" height="806" viewBox="0 0 1200 806" aria-hidden="true">
    <!-- main band -->
    <g fill="var(--clay)">
      <rect x="102" y="415" width="133" height="6"/>
      <rect x="274" y="415" width="114" height="6"/>
      <rect x="427" y="415" width="104" height="6"/>
      <rect x="570" y="415" width="105" height="6"/>
      <rect x="714" y="415" width="114" height="6"/>
      <rect x="867" y="415" width="230" height="6"/>
      <polygon points="1090,392 1110,392 1130,418 1110,444 1090,444 1110,418"/>
    </g>
    <!-- down markers -->
    <g fill="var(--sage)">
      <polygon points="67,409 82.5,417 98,409 98,425 82.5,433 67,425"/>
      <polygon points="392,409 407.5,417 423,409 423,425 407.5,433 392,425"/>
      <polygon points="679,409 694.5,417 710,409 710,425 694.5,433 679,425"/>
    </g>
    <!-- up markers -->
    <g fill="var(--slate)">
      <polygon points="239,410 254.5,402 270,410 270,426 254.5,418 239,426"/>
      <polygon points="534.5,410 550,402 565.5,410 565.5,426 550,418 534.5,426"/>
      <polygon points="831.5,410 847,402 862.5,410 862.5,426 847,418 831.5,426"/>
    </g>
    <!-- connector lines -->
    <g stroke="var(--sage)" stroke-width="1">
      <line x1="82.5" y1="437" x2="82.5" y2="464"/>
      <line x1="82.5" y1="493" x2="82.5" y2="610"/>
      <line x1="407.5" y1="437" x2="407.5" y2="464"/>
      <line x1="694.5" y1="437" x2="694.5" y2="464"/>
      <line x1="694.5" y1="493" x2="694.5" y2="565"/>
      <line x1="694.5" y1="593" x2="694.5" y2="650"/>
      <line x1="83" y1="78" x2="83" y2="147"/>
    </g>
    <g stroke="var(--slate)" stroke-width="1">
      <line x1="254.5" y1="291" x2="254.5" y2="397"/>
      <line x1="550" y1="274" x2="550" y2="397"/>
      <line x1="847" y1="81" x2="847" y2="132"/>
      <line x1="847" y1="161" x2="847" y2="219"/>
      <line x1="847" y1="248" x2="847" y2="304"/>
      <line x1="847" y1="333" x2="847" y2="397"/>
    </g>
    <!-- item chevrons -->
    <g fill="var(--sage)">
      <path transform="translate(75,469)" d="M0 0H7L15 10L7 20H0L8 10Z"/>
      <path transform="translate(75,614)" d="M0 0H7L15 10L7 20H0L8 10Z"/>
      <path transform="translate(400,469)" d="M0 0H7L15 10L7 20H0L8 10Z"/>
      <path transform="translate(687,469)" d="M0 0H7L15 10L7 20H0L8 10Z"/>
      <path transform="translate(687,569)" d="M0 0H7L15 10L7 20H0L8 10Z"/>
      <path transform="translate(687,654)" d="M0 0H7L15 10L7 20H0L8 10Z"/>
    </g>
    <g fill="var(--slate)">
      <path transform="translate(247,267)" d="M0 0H7L15 10L7 20H0L8 10Z"/>
      <path transform="translate(543,250)" d="M0 0H7L15 10L7 20H0L8 10Z"/>
      <path transform="translate(840,58)" d="M0 0H7L15 10L7 20H0L8 10Z"/>
      <path transform="translate(840,137)" d="M0 0H7L15 10L7 20H0L8 10Z"/>
      <path transform="translate(840,224)" d="M0 0H7L15 10L7 20H0L8 10Z"/>
      <path transform="translate(840,308)" d="M0 0H7L15 10L7 20H0L8 10Z"/>
    </g>
  </svg>

  <h1 class="title"><span>Our</span><span>History</span></h1>

  <!-- 2017 -->
  <div class="year is-sage" style="left:100px;top:434px">2017</div>
  <h2 class="heading is-sage" style="left:101px;top:466px">Marrowfen<br>Commences</h2>
  <p class="summary" style="left:101px;top:509px">Maren started the business<br>with 25 years' experience<br>working for government &amp;<br>non government disability &amp;<br>community services. Our<br>first office is in Ashby Vale</p>
  <h2 class="heading is-sage" style="left:101px;top:616px">NDIS Provider</h2>
  <p class="summary" style="left:101px;top:638px">Marrowfen becomes a NDIS<br>Registered provider</p>

  <!-- 2018 -->
  <h2 class="heading is-slate" style="left:275px;top:265px">Clinic<br>Expansion</h2>
  <p class="summary" style="left:275px;top:304px">Marrowfen moves offices<br>twice in Ashby Vale due to<br>growth &amp; expansion. Clinic<br>established</p>
  <div class="year is-slate" style="left:274px;top:376px">2018</div>

  <!-- 2019 -->
  <div class="year is-sage" style="left:423px;top:434px">2019</div>
  <h2 class="heading is-sage" style="left:424px;top:466px">Move to<br>Lindenmere</h2>
  <p class="summary" style="left:424px;top:509px">Marrowfen moves to<br>Lindenmere due to further<br>growth &amp; expansion</p>

  <!-- 2021 -->
  <h2 class="heading is-slate" style="left:573px;top:253px">Verity Collective</h2>
  <p class="summary" style="left:573px;top:275px">Marrowfen becomes a<br>accredited Verity Collective<br>member having met the highest<br>standards of environmental,<br>social &amp; community<br>performance</p>
  <div class="year is-slate" style="left:572px;top:376px">2021</div>

  <!-- 2022 -->
  <div class="year is-sage" style="left:721px;top:434px">2022</div>
  <h2 class="heading is-sage" style="left:722px;top:466px">Vantra Best<br>of Business</h2>
  <p class="summary" style="left:722px;top:509px">Marrowfen wins the Vantra<br>Best of Business Award (Vic)<br>for building communities</p>
  <h2 class="heading is-sage" style="left:722px;top:565px">Move to<br>Fernhollow</h2>
  <p class="summary" style="left:722px;top:609px">Marrowfen moves to a larger<br>premises in Fernhollow</p>
  <h2 class="heading is-sage" style="left:722px;top:655px">Partnerships</h2>
  <p class="summary" style="left:722px;top:680px">Partnerships established<br>with Tarawa Bay School for<br>Children with Disability &amp;<br>Wirrina Centre (Eastvale<br>University)</p>

  <!-- 2023 -->
  <h2 class="heading is-slate" style="left:871px;top:51px">Reconciliation<br>Action Plan (RAP)</h2>
  <p class="summary" style="left:871px;top:89px">Marrowfen's Reflect RAP<br>developed &amp; endorsed</p>
  <h2 class="heading is-slate" style="left:871px;top:138px">Client Advisory<br>Group</h2>
  <p class="summary" style="left:871px;top:176px">Marrowfen's Client Advisory<br>Group commences</p>
  <h2 class="heading is-slate" style="left:871px;top:224px">E-Learning<br>Platform</h2>
  <p class="summary" style="left:871px;top:262px">Marrowfen e-learning<br>platform launched</p>
  <h2 class="heading is-slate" style="left:871px;top:310px">Spectrum Mark</h2>
  <p class="summary" style="left:871px;top:333px">Marrowfen achieves<br>Spectrum Mark accreditation</p>
  <div class="year is-slate" style="left:870px;top:376px">2023</div>
</main>
</body>
</html>
```